Modern and appealing business Wordpress site

I've been operating my consulting firm for 5 years and feel like it is time to really improve on my web presence as I'm starting to get more national attention. I had a logo made through this service a couple of years ago, and would like to get a website that matches the look of it. The website will be used to (1) advertise my services (2) provide a brief overview of our management philosophies, and (3) host a resource library database. I understand HTML, but am not as familiar with how to code Wordpress, so I need someone that can help upload themes.

The website can be found at www.trbvexlane.com.

For design, I prefer round designs to square and want the color scheme to match the attached logo. I have included both the full logo and the abbreviated one.

I also have a new picture for CFO uploaded. I plan on getting a new one for the CEO in the coming weeks, so I would like someone that I could get to help make the modification at a later time.

The resource database will be put into a document library (probably Plix4) once the final design is completed rather than having multiple pages with links...just so you know the final vision for the site.

Reach out if you have any questions.

Target Market(s)

Community Action Agencies, Nonprofit Organization Leaders

Industry/Entity Type

Consulting

Coding

Coded - Design and coding required

Font styles to use
Sans Serif

Requirements
Must have
• Must match the color scheme of the attached logo

```html
<!DOCTYPE html>
<html lang="en">
<head>
<meta charset="utf-8">
<title>TR Vexlane, LLC</title>
<link href="https://fonts.googleapis.com/css2?family=Poppins:wght@300;400;500;600;700&display=swap" rel="stylesheet">
<style>
:root{
  --blue:#2e9fd8;
  --blue-deep:#0c75b9;
  --ink:#1c1c1c;
  --text:#555;
  --muted:#8a8a8a;
  --grey-bg:#f2f2f2;
  --bar:#555555;
  --white:#fff;
}
*{margin:0;padding:0;box-sizing:border-box}
html,body{width:1200px;height:3497px;overflow:hidden;background:var(--white)}
body{font-family:'Poppins',sans-serif;color:var(--text)}
.page{position:relative;width:1200px;height:3497px;overflow:hidden}
.abs{position:absolute}

/* hero */
.hero-photo{left:0;top:0;width:1200px;height:710px;
  background:radial-gradient(circle at 86% 12%,#fffbe0 0,#f3e98a 8%,#9cc43a 22%,transparent 45%),
  radial-gradient(circle at 35% 45%,#8fc23c 0,#4f8a28 30%,transparent 60%),
  linear-gradient(180deg,#5f8b2c 0%,#6b6a3a 45%,#5c3f3c 70%,#3b2824 100%)}
.hero-wave{left:0;top:540px}
.site-header{left:166px;top:23px;width:870px;height:79px;background:var(--white);
  border-radius:0 0 0 34px;box-shadow:0 4px 14px rgba(0,0,0,.12)}
.brand{left:22px;top:18px;display:flex;align-items:center;gap:8px}
.brand-dot{width:40px;height:40px;border-radius:50%;background:var(--blue)}
.brand-name{font-weight:700;font-size:30px;color:var(--blue);letter-spacing:1px}
.main-nav{left:438px;top:28px;display:flex;gap:28px;font-size:12px;font-weight:500;color:#444}
.main-nav a{color:inherit;text-decoration:none;position:relative}
.main-nav a.active::after{content:"";position:absolute;left:-2px;right:-2px;top:45px;height:4px;background:var(--blue)}
.hero-copy{left:619px;top:252px;width:418px;color:var(--white)}
.hero-kicker{font-weight:300;font-size:33px;line-height:1.1;letter-spacing:-.3px}
.hero-title{font-weight:700;font-size:47px;line-height:1.05;margin-top:2px}
.hero-text{font-size:13.6px;line-height:21.4px;margin-top:12px;text-align:justify}
.hero-chevron{left:586px;top:624px}

/* services */
.section-title{font-size:38px;color:var(--ink);font-weight:400;line-height:1}
.section-title b{font-weight:700}
.services-title{left:164px;top:795px}
.service{top:880px;width:256px}
.service-img{width:256px;height:241px}
.service h3{font-size:19px;font-weight:500;color:var(--ink);margin-top:24px}
.service p{font-size:13.2px;line-height:21.4px;color:var(--text);margin-top:10px;text-align:justify}

/* mission */
.mission-band{left:0;top:1513px;width:1200px;height:465px;background:linear-gradient(90deg,#3eb0e6 0%,#1c8fd0 50%,var(--blue-deep) 100%)}
.mission-copy{left:634px;top:1672px;width:410px;color:var(--white)}
.mission-copy .section-title{color:var(--white)}
.mission-copy p{font-size:19.5px;line-height:27.6px;margin-top:18px}

/* testimonials */
.testimonials-title{left:164px;top:2080px}
.testimonial{top:2156px;width:416px;height:301px;background:var(--white);
  border-top:14px solid var(--blue);border-bottom:14px solid var(--blue);
  border-right:2px solid var(--blue);border-top-right-radius:56px;border-bottom-left-radius:56px;
  box-shadow:0 6px 18px rgba(0,0,0,.06)}
.quote-open,.quote-close{position:absolute;font-size:90px;font-weight:700;color:#dcdcdc;line-height:1}
.quote-open{left:22px;top:10px}
.quote-close{right:26px;bottom:-30px}
.testimonial p{position:absolute;left:22px;right:22px;font-size:12.6px;line-height:21.4px;color:var(--text)}
.testimonial .rule{position:absolute;left:22px;width:22px;height:3px;background:var(--blue)}
.testimonial cite{position:absolute;left:22px;font-style:normal;font-size:12.6px;font-weight:500;color:#444}
.slider-arrow{top:2286px}

/* team */
.team-bg{left:0;top:2596px;width:1200px;height:900px;background:var(--grey-bg)}
.team-divider{left:600px;top:2733px;width:1px;height:355px;background:#cfcfcf}
.member{top:2728px;width:320px;text-align:center}
.member-photo{width:300px;height:300px;border-radius:50%;margin:0 auto;border:8px solid var(--white);box-shadow:0 4px 16px rgba(0,0,0,.12)}
.member-role{font-size:19px;color:var(--ink);margin-top:18px;line-height:1.3}
.member-name{font-size:16.5px;color:#444;margin-top:4px}

/* footer */
.footer-wave{left:0;top:3100px}
.footer-brand{left:166px;top:3333px;display:flex;align-items:center;gap:8px}
.footer-brand .brand-dot{background:var(--white);width:36px;height:36px}
.footer-brand .brand-name{color:var(--white);font-size:28px}
.footer-col{top:3250px;height:205px;border-left:1px solid rgba(255,255,255,.45);color:var(--white)}
.footer-col h4{font-size:15px;font-weight:500;margin-top:48px}
.footer-col ul{list-style:none;margin-top:8px}
.footer-col li{font-size:11.5px;line-height:19px}
.contact-item{display:flex;align-items:flex-start;gap:10px;font-size:11.3px;line-height:19px}
.contact-item svg{flex:none;margin-top:4px}
.social{display:flex;gap:10px;margin-top:8px}
.social span{width:10px;height:10px;border-radius:50%;background:var(--white)}
.copyright{left:0;top:3468px;width:1200px;height:29px;background:var(--bar);color:#e8e8e8;font-size:11px;text-align:center;line-height:29px}
</style>
</head>
<body>
<div class="page">

  <!-- hero -->
  <div class="abs hero-photo" role="img" aria-label="Hand pouring water drops onto a young seedling growing from soil in warm sunlight"></div>
  <svg class="abs hero-wave" width="1200" height="180" viewBox="0 540 1200 180" aria-hidden="true">
    <path d="M0,665 C320,720 720,720 1200,557 L1200,720 L0,720 Z" fill="#fff"/>
  </svg>

  <header class="abs site-header">
    <div class="abs brand"><span class="brand-dot"></span><span class="brand-name">VEXLANE</span></div>
    <nav class="abs main-nav">
      <a class="active">Home</a><a>Services</a><a>Roma</a><a>Madd</a><a>Resources</a><a>Contact</a>
    </nav>
  </header>

  <section class="abs hero-copy">
    <div class="hero-kicker">LEADING ORGANIZATIONS</div>
    <h1 class="hero-title">TO EXCELLENCE!</h1>
    <p class="hero-text">TR Vexlane, LLC was created to help nonprofits and government contractors meet their basic funding requirements and adopt a Mission Aligned Data Driven mindset that promotes positive change in the lives of the people they serve. Our approach is not simply based off of theoretical business practices, but on practical solutions to real-life situations learned through more than twenty years of experience.</p>
  </section>
  <svg class="abs hero-chevron" width="28" height="18" viewBox="0 0 28 18" aria-hidden="true"><path d="M2,3 L14,14 L26,3" fill="none" stroke="#fff" stroke-width="2"/></svg>

  <!-- services -->
  <h2 class="abs section-title services-title">OUR <b>SERVICES</b></h2>

  <article class="abs service" style="left:164px">
    <div class="service-img" role="img" aria-label="Hands reviewing printed charts beside a laptop" style="border-radius:0 40px 0 40px;background:linear-gradient(135deg,#d9d6d2,#f1efec 50%,#9a928a)"></div>
    <h3>Training &amp; Consulting</h3>
    <p>We are dedicated to the success of our customers and offer a variety of services focused on improving organizational efficiency and effectiveness through implementation of the Mission Aligned Data Driven (MADD) mindset and the Results Oriented Management and Accountability (ROMA) system of organizational management.</p>
  </article>

  <article class="abs service" style="left:472px">
    <div class="service-img" role="img" aria-label="Glowing cyan and red bar chart with binary digits" style="border-radius:40px 0 40px 0;background:linear-gradient(160deg,#0f3e4a,#0e6f7a 45%,#23c3d9 75%,#b0402e)"></div>
    <h3>Data Analytics</h3>
    <p>One the most important, and frequently neglected, areas of organizational management is the analysis of data to accurately identify community needs and track progress towards the successful fulfillment of the entity's purpose. Our goal is to ensure each of our customers is equipped with the tools necessary to obtain objective data that will allow for quality decision making.</p>
  </article>

  <article class="abs service" style="left:781px">
    <div class="service-img" role="img" aria-label="Tablet with film strip and floating story cards" style="border-radius:40px 0 40px 0;background:linear-gradient(160deg,#f4f4f4,#dcdcdc 60%,#bdbdbd)"></div>
    <h3>Storytelling</h3>
    <p>TR Vexlane, LLC is dedicated to ensuring each of our customers is provided with the tools necessary to tell their story through the generation of graphic reports, outreach tools, and videos so they can increase community support and involvement, allowing for a reduced reliance on government funding.</p>
  </article>

  <!-- mission -->
  <div class="abs mission-band"></div>
  <svg class="abs" style="left:0;top:1513px" width="600" height="465" viewBox="0 1513 600 465" role="img" aria-label="Close-up of a compass dial reading mission">
    <defs><radialGradient id="dial" cx="0" cy="1" r="1"><stop offset="0" stop-color="#cfd3d8"/><stop offset=".5" stop-color="#f6f7f9"/><stop offset="1" stop-color="#ffffff"/></radialGradient></defs>
    <path d="M0,1513 L217,1513 C430,1570 600,1760 597,1978 L0,1978 Z" fill="url(#dial)"/>
  </svg>
  <section class="abs mission-copy">
    <h2 class="section-title">OUR <b>MISSION</b></h2>
    <p>To help social service organizations develop a Mission Aligned Data Driven mindset that promotes positive change in the lives of the customers they serve.</p>
  </section>

  <!-- testimonials -->
  <h2 class="abs section-title testimonials-title"><b>TESTIMONIALS</b></h2>
  <svg class="abs slider-arrow" style="left:88px" width="16" height="30" viewBox="0 0 16 30" aria-hidden="true"><path d="M13,2 L3,15 L13,28" fill="none" stroke="#2e9fd8" stroke-width="2"/></svg>
  <svg class="abs slider-arrow" style="left:1114px" width="16" height="30" viewBox="0 0 16 30" aria-hidden="true"><path d="M3,2 L13,15 L3,28" fill="none" stroke="#2e9fd8" stroke-width="2"/></svg>

  <blockquote class="abs testimonial" style="left:166px">
    <span class="quote-open">&ldquo;</span>
    <p style="top:88px">It was a training, but not your typical training. It leaves you with a new and different take on things. You will find yourself saying 'Wow, I've never thought of it like that before'. You will be left with new and refreshing ideas and different ways to approach situations.</p>
    <span class="rule" style="top:204px"></span>
    <cite style="top:224px">Marlow County Senior Services</cite>
    <span class="quote-close">&rdquo;</span>
  </blockquote>

  <blockquote class="abs testimonial" style="left:620px">
    <span class="quote-open">&ldquo;</span>
    <p style="top:98px">Reed is easy to work with and his expertise allows you to tailor your training to the specific needs of your agency. We highly recommend Reed and his company.</p>
    <span class="rule" style="top:171px"></span>
    <cite style="top:190px">Community Action Partnership of Westbrook Valley</cite>
    <span class="quote-close">&rdquo;</span>
  </blockquote>

  <!-- team -->
  <div class="abs team-bg"></div>
  <div class="abs team-divider"></div>
  <div class="abs member" style="left:219px">
    <div class="member-photo" role="img" aria-label="Portrait photo of the CEO" style="background:linear-gradient(160deg,#b9c7a2,#7f8f6a 55%,#2c3242)"></div>
    <div class="member-role">CEO</div>
    <div class="member-name">DORIAN "REED" VEXLANE</div>
  </div>
  <div class="abs member" style="left:660px">
    <div class="member-photo" role="img" aria-label="Portrait photo of the CFO" style="background:linear-gradient(160deg,#6e8a5a,#b49a7a 50%,#3f9a5b)"></div>
    <div class="member-role">CFO</div>
    <div class="member-name">MIRA CALDER VEXLANE</div>
  </div>

  <!-- footer -->
  <svg class="abs footer-wave" width="1200" height="370" viewBox="0 3100 1200 370" aria-hidden="true">
    <path d="M0,3251 C420,3275 900,3250 1200,3109 L1200,3470 L0,3470 Z" fill="#2e9fd8"/>
  </svg>
  <footer>
    <div class="abs footer-brand"><span class="brand-dot"></span><span class="brand-name">VEXLANE</span></div>

    <div class="abs footer-col" style="left:381px;padding-left:24px;width:222px">
      <h4 style="margin-top:56px">Services</h4>
      <ul><li>Training &amp; Consulting</li><li>Data Analytics</li><li>Storytelling</li></ul>
    </div>
    <div class="abs footer-col" style="left:603px;padding-left:25px;width:221px">
      <h4>Navigation</h4>
      <ul><li>Home</li><li>Services</li><li>Roma</li><li>Madd</li><li>Resources</li><li>Contact</li></ul>
    </div>
    <div class="abs footer-col" style="left:824px;padding-left:26px;width:300px">
      <h4>Contact Us</h4>
      <div style="margin-top:10px">
        <div class="contact-item"><svg width="11" height="11" viewBox="0 0 24 24"><path d="M6.6 10.8a15 15 0 006.6 6.6l2.2-2.2c.3-.3.7-.4 1-.2 1.1.4 2.3.6 3.6.6.6 0 1 .4 1 1V20c0 .6-.4 1-1 1A17 17 0 013 4c0-.6.4-1 1-1h3.5c.6 0 1 .4 1 1 0 1.3.2 2.5.6 3.6.1.3 0 .7-.2 1z" fill="#fff"/></svg><span>+61 3555 0192</span></div>
        <div class="contact-item"><svg width="11" height="11" viewBox="0 0 24 24"><path d="M2 5h20v14H2z" fill="#fff"/><path d="M2 5l10 8 10-8" fill="none" stroke="#2e9fd8" stroke-width="2"/></svg><span>support@trbvexlane.com</span></div>
        <div class="contact-item"><svg width="11" height="13" viewBox="0 0 24 28"><path d="M12 0a9 9 0 00-9 9c0 7 9 19 9 19s9-12 9-19a9 9 0 00-9-9zm0 12a3 3 0 110-6 3 3 0 010 6z" fill="#fff"/></svg><span>24/8 Harlow St, Brookvale<br>VIC 3999, Australia</span></div>
        <div class="social"><span></span><span></span><span></span></div>
      </div>
    </div>

    <div class="abs copyright">Copyright © 2022 Vexlane LLC. All Rights Reserved</div>
  </footer>
</div>
</body>
</html>
```